Plumbing & Heating company

A leaflet containing -

Company name - Brackenfold Plumbing Solutions
logo
Mobile number - 07700 914226
Landline - 01632 870512
Email - Info@brackenfoldplumbing.example.co.uk
website - Brackenfold-plumbing.example.co.uk
Social media logos - pixgram, Chatterly

services we offer

- Boiler replacements (free quote)
- General plumbing & heating
- Tap replacements
- 1st & 2nd
- New builds & Extensions
- Cylinder replcemets

```html
<!DOCTYPE html>
<html lang="en">
<head>
<meta charset="utf-8">
<title>Brackenfold Plumbing Solutions – Leaflet</title>
<link rel="stylesheet" href="https://fonts.googleapis.com/css2?family=Orbitron:wght@700;900&family=Montserrat:wght@600;700&display=swap">
<style>
  :root {
    --blue: #0b63a8;
    --orange: #f24a2e;
    --yellow: #f5b21b;
    --white: #ffffff;
    --ink: #1a4f86;
    --photo-dark: #3a3430;
    --photo-mid: #7a6a5a;
    --photo-light: #d9d2c8;
  }
  * { margin: 0; padding: 0; box-sizing: border-box; }
  html, body { width: 877px; height: 1200px; overflow: hidden; background: #ffffff; }
  body { font-family: "Montserrat", sans-serif; color: var(--white); }
  .leaflet { position: relative; width: 877px; height: 1200px; background: var(--blue); overflow: hidden; }

  .logo-box { position: absolute; left: 0; top: 0; width: 454px; height: 155px; background: var(--white);
    display: flex; align-items: center; justify-content: center; gap: 12px; }
  .logo-mark { width: 34px; height: 34px; border-radius: 50%; background: var(--orange); }
  .logo-name { font-family: "Orbitron", sans-serif; font-weight: 900; font-size: 30px; color: var(--ink); letter-spacing: 1px; }

  .photo { position: absolute; right: 0; width: 423px; }
  .photo-plumber { top: 0; height: 725px; background: linear-gradient(160deg, var(--photo-light) 0%, var(--photo-mid) 35%, var(--photo-dark) 70%, #1f2b55 100%); }
  .photo-basin { top: 731px; height: 379px; background: linear-gradient(200deg, #eeeae4 0%, var(--photo-light) 45%, #4a5f9c 100%); }

  .intro { position: absolute; left: 40px; top: 240px; width: 390px; }
  .title { font-family: "Orbitron", sans-serif; font-weight: 900; font-size: 37px; line-height: 0.95; letter-spacing: 0.5px; }
  .title-sub { display: block; font-family: "Orbitron", sans-serif; font-weight: 700; font-size: 22px; letter-spacing: 21px; margin-top: 4px; }
  .intro-text { font-weight: 700; font-size: 17.5px; line-height: 1.35; margin-top: 30px; }

  .services-band { position: absolute; left: 0; top: 551px; width: 475px; height: 94px; background: var(--orange);
    padding: 14px 0 0 40px; font-family: "Orbitron", sans-serif; font-weight: 900; line-height: 0.95; }
  .services-band .line1 { font-size: 29px; display: block; }
  .services-band .line2 { font-size: 35px; display: block; }

  .services { position: absolute; left: 40px; top: 680px; width: 376px; list-style: none; }
  .service { display: flex; align-items: center; gap: 12px; padding: 6px 0 8px; border-bottom: 2px dashed rgba(255,255,255,0.7); }
  .service:last-child { border-bottom: none; }
  .service-icon { flex: 0 0 44px; width: 44px; height: 44px; }
  .service-name { font-weight: 700; font-size: 24px; line-height: 1.05; }

  .contact-band { position: absolute; left: 0; top: 1110px; width: 877px; height: 90px; background: var(--orange);
    display: flex; align-items: center; padding: 0 0 0 44px; }
  .phones { font-weight: 700; font-size: 25px; line-height: 1.1; width: 250px; }
  .web { font-weight: 600; font-size: 14.5px; line-height: 1.75; width: 430px; }
  .contact-row { display: flex; align-items: center; gap: 8px; white-space: nowrap; }
  .socials { display: flex; flex-direction: column; gap: 2px; font-weight: 700; font-size: 14px; }
</style>
</head>
<body>
<main class="leaflet">
  <header class="logo-box">
    <span class="logo-mark"></span>
    <span class="logo-name">BRACKENFOLD</span>
  </header>

  <div class="photo photo-plumber" role="img" aria-label="Smiling plumber in blue cap and overalls holding an adjustable wrench in a kitchen"></div>
  <div class="photo photo-basin" role="img" aria-label="Plumber fitting a tap on a bathroom basin beside a round mirror"></div>

  <section class="intro">
    <h1 class="title">BRACKENFOLD<br>PLUMBING<span class="title-sub">SOLUTIONS</span></h1>
    <p class="intro-text">Brackenfold Plumbing &amp; Heating contractor based in Hampshire and covering Winchester and the surrounding areas.</p>
  </section>

  <h2 class="services-band"><span class="line1">SERVICES</span><span class="line2">WE OFFER</span></h2>

  <svg width="0" height="0" style="position:absolute">
    <defs>
      <symbol id="ring" viewBox="0 0 44 44">
        <circle cx="22" cy="22" r="20" fill="#fff" stroke="#f24a2e" stroke-width="3"/>
        <circle cx="22" cy="22" r="16" fill="none" stroke="#f5b21b" stroke-width="1.5"/>
      </symbol>
    </defs>
  </svg>

  <ul class="services">
    <li class="service">
      <svg class="service-icon" viewBox="0 0 44 44"><use href="#ring"/><rect x="15" y="13" width="14" height="18" rx="2" fill="none" stroke="#1a4f86" stroke-width="2"/><circle cx="22" cy="24" r="3" fill="none" stroke="#1a4f86" stroke-width="1.8"/></svg>
      <span class="service-name">Boiler replacements<br>(free quote)</span>
    </li>
    <li class="service">
      <svg class="service-icon" viewBox="0 0 44 44"><use href="#ring"/><path d="M15 14v10a7 7 0 0 0 14 0v-10" fill="none" stroke="#1a4f86" stroke-width="2.4"/></svg>
      <span class="service-name">General plumbing &amp;<br>heating</span>
    </li>
    <li class="service">
      <svg class="service-icon" viewBox="0 0 44 44"><use href="#ring"/><path d="M13 18h14v5h-4v4M20 14h6" fill="none" stroke="#1a4f86" stroke-width="2.2"/><circle cx="23" cy="31" r="1.6" fill="#1a4f86"/></svg>
      <span class="service-name">Tap replacements</span>
    </li>
    <li class="service">
      <svg class="service-icon" viewBox="0 0 44 44"><use href="#ring"/><path d="M14 30l16-16M14 14l16 16" stroke="#1a4f86" stroke-width="2.4" stroke-linecap="round"/></svg>
      <span class="service-name">1st &amp; 2nd</span>
    </li>
    <li class="service">
      <svg class="service-icon" viewBox="0 0 44 44"><use href="#ring"/><path d="M13 22l9-8 9 8M16 20v10h12V20" fill="none" stroke="#1a4f86" stroke-width="2.2"/></svg>
      <span class="service-name">New builds &amp;<br>Extensions</span>
    </li>
    <li class="service">
      <svg class="service-icon" viewBox="0 0 44 44"><use href="#ring"/><rect x="16" y="14" width="12" height="18" rx="5" fill="none" stroke="#1a4f86" stroke-width="2.2"/><path d="M22 19c-2 3-2 5 0 6 2-1 2-3 0-6z" fill="#1a4f86"/></svg>
      <span class="service-name">Cylinder replcemets</span>
    </li>
  </ul>

  <footer class="contact-band">
    <div class="phones">
      <div class="contact-row">
        <svg width="18" height="18" viewBox="0 0 24 24"><path d="M6 3l4 4-2 3c1 3 3 5 6 6l3-2 4 4-3 3C10 21 3 14 3 6z" fill="#fff"/></svg>
        07700 914226
      </div>
      <div class="contact-row">
        <svg width="18" height="18" viewBox="0 0 24 24"><rect x="3" y="10" width="18" height="11" rx="2" fill="#fff"/><path d="M2 8c3-4 17-4 20 0v2h-5V8H7v2H2z" fill="#fff"/></svg>
        01632 870512
      </div>
    </div>
    <div class="web">
      <div class="contact-row">
        <svg width="16" height="16" viewBox="0 0 24 24"><rect x="2" y="5" width="20" height="14" rx="3" fill="#fff"/><path d="M3 7l9 6 9-6" fill="none" stroke="#f24a2e" stroke-width="2"/></svg>
        Info@brackenfoldplumbing.example.co.uk
      </div>
      <div class="contact-row">
        <svg width="16" height="16" viewBox="0 0 24 24"><circle cx="12" cy="12" r="10" fill="none" stroke="#fff" stroke-width="2"/><path d="M2 12h20M12 2c-4 5-4 15 0 20M12 2c4 5 4 15 0 20" fill="none" stroke="#fff" stroke-width="1.6"/></svg>
        www.brackenfold-plumbing.example.co.uk
      </div>
    </div>
    <div class="socials">
      <span>pixgram</span>
      <span>Chatterly</span>
    </div>
  </footer>
</main>
</body>
</html>
```